New Webpage for High Class Expert Witness Services Company

We are looking for a minimalist design for a webpage that just has our logo and an entry form offer to connect with one of our Liaisons.
The entry form should just ask for Name, Email, Contact Info and Description of Project.

Company Name is: The Marlow Crest Advisory Services

Number of Pages Required

1 page

```html
<!DOCTYPE html>
<html lang="en">
<head>
<meta charset="utf-8">
<title>Marlow Crest Advisory Services – Connect with Our Liaisons</title>
<link href="https://fonts.googleapis.com/css2?family=Montserrat:wght@400;500;600&display=swap" rel="stylesheet">
<style>
  :root {
    --bg-center: #3e3e3e;
    --bg-edge: #0f0f0f;
    --card: #1b1b1b;
    --field: #242424;
    --accent: #3399cc;
    --rule: #1266c8;
    --text: #ffffff;
    --muted: #a8a8a8;
    --placeholder: #b3b3b3;
    --brand: #d6d6d6;
    --footer: #9a9a9a;
  }
  * { box-sizing: border-box; margin: 0; padding: 0; }
  html, body { width: 1200px; height: 663px; overflow: hidden; }
  body {
    position: relative;
    font-family: "Montserrat", sans-serif;
    background: radial-gradient(ellipse 55% 60% at 50% 30%, var(--bg-center), var(--bg-edge));
  }
  .brand {
    position: absolute; top: 62px; left: 0; width: 1200px;
    display: flex; justify-content: center; align-items: center; gap: 12px;
  }
  .brand-mark { width: 14px; height: 14px; background: var(--brand); }
  .brand-name {
    color: var(--brand); font-weight: 500; font-size: 22px; letter-spacing: 1px;
  }
  .contact-card {
    position: absolute; left: 284px; top: 177px; width: 632px; height: 398px;
    background: var(--card); border-radius: 8px;
    box-shadow: 0 10px 40px rgba(0,0,0,0.35);
  }
  .card-accent {
    position: absolute; left: 29px; top: 0; width: 575px; height: 6px;
    background: var(--accent); border-radius: 0 0 3px 3px;
  }
  .card-title {
    position: absolute; left: 33px; top: 26px;
    color: var(--text); font-weight: 600; font-size: 17.5px;
  }
  .card-subtitle {
    position: absolute; left: 33px; top: 53px;
    color: var(--muted); font-size: 12px;
  }
  .card-rule {
    position: absolute; left: 32px; top: 81px; width: 568px; height: 1px; background: var(--rule);
  }
  .card-rule::before {
    content: ""; position: absolute; left: 0; top: -1px; width: 126px; height: 3px; background: var(--rule);
  }
  .form-field {
    position: absolute; left: 32px; width: 568px; height: 35px;
    background: var(--field); border-radius: 3px;
    color: var(--placeholder); font-size: 10px; font-weight: 500; letter-spacing: 0.2px;
    padding: 11px 14px; line-height: 13px;
  }
  .field-name { top: 98px; }
  .field-email { top: 142px; }
  .field-phone { top: 186px; }
  .field-description { top: 230px; height: 95px; }
  .submit-button {
    position: absolute; left: 32px; top: 335px; width: 568px; height: 35px;
    background: var(--accent); border-radius: 3px;
    color: var(--text); font-size: 9.5px; font-weight: 600; letter-spacing: 0.5px;
    display: flex; align-items: center; justify-content: center;
  }
  .site-footer {
    position: absolute; left: 0; top: 620px; width: 1200px; text-align: center;
    color: var(--footer); font-size: 8px; letter-spacing: 0.4px;
  }
</style>
</head>
<body>
  <header class="brand">
    <span class="brand-mark"></span>
    <span class="brand-name">MARLOW CREST ADVISORY SERVICES</span>
  </header>

  <section class="contact-card">
    <div class="card-accent"></div>
    <h1 class="card-title">Connect with Our Liaisons</h1>
    <p class="card-subtitle">Please fill out the form below.</p>
    <div class="card-rule"></div>
    <div class="form-field field-name">Your Name</div>
    <div class="form-field field-email">Your Email</div>
    <div class="form-field field-phone">Your Phone Number</div>
    <div class="form-field field-description">Description of Project</div>
    <div class="submit-button">SUBMIT</div>
  </section>

  <footer class="site-footer">COPYRIGHT © 2026 MARLOW CREST ADVISORY SERVICES. ALL RIGHTS RESERVED.</footer>
</body>
</html>
```